Lean Plate Daily Promo Postcard

Need 4x6 postcard created and similarly deisgned as attached postcard example. I have provided client notes:

Side A

(Left aligned image of fit cartoon chick - branded if possible)

“You'll love being Lean Plate Daily!" (company name in another color)

Text paragraph:

Lean Plate Daily is the most convenient, affordable, and flexible way to eat healthy, super nutritious, and squeaky clean food with a taste you’ll love!

Our meals are always freshly prepared, never frozen! We use the purest, local ingredients we can find, so forget about preservatives here and pesticides. All entrees are fitness focused and made to order. That means we can make your meals the way you want them, allowing us to accommodate:

-All Food Allergies
-Vegan Diets
-Paleo Diets
-Diets dictated by Personal Trainers & Doctors
-Or just plain picky eaters (you know who you are)

(Right aligned image bleed of healthy food dish)

Side B

(Upper left aligned Lean Plate Daily logo)

Reasons Why We Are Awesome:

- You get to choose your meals. We're here to help if you need us, but you won't get two of anything unless you ask for it!

-No contracts or hefty monthly fees. Seriously, no need to even cancel - you only pay for what you order. Sound good? Fist bump?

-We will be best friends! When you sign up with us, you get your own Lean Plate Daily advisor who will be by your side to help you make the right food choices and work with you to make us better for you. How cool is that!?

-We will pay you to promote us! You're not hallucinating. We pay more than ANY other healthy meal delivery company out there. Not only that but we pay it for as long as your friends stay our friends! Ask your advisor for details.

(Mid left aligned starburst call-to-action — “FREE Delivery For Life!”)

(Right aligned image of fit cartoon guy — branded if possible — message bubble — “Call us today to get started 833-415-2967”)

(Bottom centered web url no www - just = LeanPlateDaily.com)

```html
<!DOCTYPE html>
<html lang="en">
<head>
<meta charset="utf-8">
<title>Lean Plate Daily Promo Postcard</title>
<link rel="stylesheet" href="https://fonts.googleapis.com/css2?family=Questrial&family=Nunito:ital,wght@0,700;0,800;0,900;1,800&family=Arimo:wght@400;700&display=swap">
<style>
  :root {
    --page: #d9d9d9;
    --white: #ffffff;
    --sky: #5cc6ee;
    --sky-deep: #2fa9e0;
    --brand: #1a9fd0;
    --brand-deep: #1487c4;
    --ink: #333333;
    --body: #555555;
    --green: #3fae3a;
    --green-light: #6fcf4a;
    --skin: #f2c9a6;
    --hair: #d8401f;
    --plate: #2f4f7a;
    --food: #c9583a;
  }
  * { box-sizing: border-box; margin: 0; padding: 0; }
  html, body { width: 796px; height: 1200px; overflow: hidden; }
  body { background: var(--page); font-family: "Arimo", Arial, sans-serif; position: relative; }

  .card {
    position: absolute; left: 29px; width: 740px; height: 573px;
    overflow: hidden; background: var(--white);
  }
  .card--front { top: 20px; }
  .card--back { top: 607px; }

  .sunburst {
    position: absolute; inset: 0;
    background: radial-gradient(ellipse at 62% 45%, var(--white) 0%, var(--white) 42%, #bfe8f8 62%, var(--sky) 85%, var(--sky-deep) 100%);
  }
  .card--back .sunburst {
    background: radial-gradient(ellipse at 78% 40%, #bfe8f8 0%, var(--sky) 45%, var(--sky-deep) 100%);
    left: 300px;
  }
  .card--back .sunburst-fade {
    position: absolute; top: 0; bottom: 0; left: 0; width: 470px;
    background: linear-gradient(90deg, var(--white) 70%, rgba(255,255,255,0) 100%);
  }

  .figure { position: absolute; }
  .figure--woman {
    left: 24px; top: 0; width: 282px; height: 573px;
    background: linear-gradient(180deg, var(--hair) 0%, #e8703f 30%, var(--skin) 45%, var(--green-light) 65%, var(--skin) 85%);
    border-radius: 140px 140px 40px 40px; opacity: .9;
  }
  .figure--man {
    left: 472px; top: 7px; width: 263px; height: 566px;
    background: linear-gradient(180deg, #2b2b2b 0%, #e0a85a 22%, #f2c37a 45%, #fbf3e4 70%, #e0a85a 100%);
    border-radius: 130px 130px 30px 30px; opacity: .9;
  }
  .photo { position: absolute; }
  .photo--pasta {
    left: 565px; top: 405px; width: 190px; height: 190px; border-radius: 50%;
    background: radial-gradient(circle, #f0c060 0%, var(--food) 45%, #8a3a22 62%, var(--plate) 66%, #1f3656 100%);
  }
  .photo--chicken {
    left: 4px; top: 460px; width: 215px; height: 113px;
    background: radial-gradient(ellipse at 50% 60%, #c89a6a 0%, #8a5a34 45%, #4f7a3a 80%, #36552a 100%);
    border-radius: 0 60px 0 0;
  }

  /* Front */
  .headline { position: absolute; left: 277px; top: 18px; width: 450px; }
  .headline-lead { font-family: "Questrial", sans-serif; font-size: 44px; color: var(--ink); line-height: 1.1; }
  .headline-brand { font-family: "Nunito", sans-serif; font-weight: 900; font-size: 48px; color: var(--brand); line-height: 1.15; }
  .tagline {
    position: absolute; left: 292px; top: 140px; width: 430px; text-align: center;
    font-family: "Nunito", sans-serif; font-style: italic; font-weight: 800;
    font-size: 18px; line-height: 1.2; color: var(--brand-deep);
  }
  .intro {
    position: absolute; left: 316px; top: 236px; width: 262px; text-align: center;
    font-size: 13px; line-height: 1.3; color: var(--body);
  }
  .checklist { position: absolute; left: 318px; top: 364px; width: 240px; list-style: none; }
  .checklist li {
    display: flex; align-items: flex-start; gap: 6px;
    font-weight: 700; font-size: 14.5px; color: var(--ink); line-height: 1.27;
  }
  .checklist .tick { margin-top: 1px; }
  .tick { width: 17px; height: 17px; flex: none; }

  .burst { position: absolute; display: flex; align-items: center; justify-content: center; text-align: center; z-index: 2; }
  .burst svg { position: absolute; inset: 0; width: 100%; height: 100%; }
  .burst span {
    position: relative; font-family: "Nunito", sans-serif; font-weight: 900;
    color: var(--white); line-height: 1.05;
  }
  .burst--price { left: 588px; top: 268px; width: 136px; height: 136px; }
  .burst--price span { font-size: 21px; }
  .burst--delivery { left: 145px; top: 453px; width: 105px; height: 105px; }
  .burst--delivery span { font-size: 17px; }

  .banner {
    position: absolute; left: 211px; top: 510px; width: 413px; height: 28px; z-index: 2;
    border-radius: 14px; background: var(--green);
    font-family: "Nunito", sans-serif; font-style: italic; font-weight: 800;
    font-size: 15px; color: var(--white); text-align: center; line-height: 28px;
  }

  /* Back */
  .wordmark {
    position: absolute; left: 26px; top: 104px; display: flex; align-items: center; gap: 7px;
    font-family: "Nunito", sans-serif; font-weight: 800; font-size: 15px; color: var(--brand);
  }
  .wordmark i { width: 18px; height: 18px; border-radius: 50%; background: var(--brand); display: block; }
  .reasons-title { position: absolute; left: 196px; top: 40px; width: 275px; font-family: "Nunito", sans-serif; font-weight: 800; line-height: 1.08; }
  .reasons-title .light { color: var(--sky); font-size: 31px; display: block; }
  .reasons-title .brand { color: var(--brand); font-size: 32px; font-weight: 900; display: block; }
  .reasons { position: absolute; left: 22px; top: 166px; width: 300px; list-style: none; }
  .reasons li {
    display: flex; gap: 6px; font-size: 11.5px; line-height: 1.3; color: var(--body); margin-bottom: 7px;
  }
  .reasons .tick { width: 14px; height: 14px; margin-top: 1px; }

  .bubble {
    position: absolute; left: 300px; top: 430px; width: 182px; height: 80px; z-index: 2;
    background: var(--brand-deep); border-radius: 16px; color: var(--white); text-align: center;
    font-family: "Nunito", sans-serif; font-weight: 800; font-size: 18px; line-height: 1.15; padding-top: 8px;
  }
  .bubble::after {
    content: ""; position: absolute; right: -16px; top: 28px;
    border-left: 20px solid var(--brand-deep); border-top: 10px solid transparent; border-bottom: 10px solid transparent;
  }
  .bubble .phone { font-size: 20px; font-weight: 900; }
  .web-address {
    position: absolute; left: 252px; top: 520px; width: 240px; text-align: center; z-index: 2;
    font-family: "Nunito", sans-serif; font-weight: 900; font-size: 22px; color: var(--brand-deep);
  }
</style>
</head>
<body>
<svg width="0" height="0" style="position:absolute">
  <defs>
    <polygon id="starburst" points="100,50 89.6,60.6 93.3,75 79,79 75,93.3 60.6,89.6 50,100 39.4,89.6 25,93.3 21,79 6.7,75 10.4,60.6 0,50 10.4,39.4 6.7,25 21,21 25,6.7 39.4,10.4 50,0 60.6,10.4 75,6.7 79,21 93.3,25 89.6,39.4"/>
    <symbol id="tick-mark" viewBox="0 0 20 20"><path d="M3 10.5 L8 15.5 L17 4.5" fill="none" stroke="#3fae3a" stroke-width="3.5" stroke-linecap="round" stroke-linejoin="round"/></symbol>
  </defs>
</svg>

<section class="card card--front">
  <div class="sunburst"></div>
  <div class="figure figure--woman" role="img" aria-label="Cartoon illustration of a fit red-haired woman in green workout wear"></div>
  <div class="photo photo--pasta" role="img" aria-label="Photo of a healthy pasta dish with vegetables and chicken"></div>

  <h1 class="headline">
    <span class="headline-lead">You'll love being</span><br>
    <span class="headline-brand">Lean Plate Daily!</span>
  </h1>
  <p class="tagline">Lean Plate Daily is the most convenient, affordable, and flexible way to eat healthy, super nutritious, and squeaky clean food with a taste you’ll love!</p>
  <p class="intro">Our meals are always freshly prepared, never frozen! We use the purest, local ingredients we can find, so forget about preservatives here and pesticides. All entrees are fitness focused and made to order. That means we can make your meals the way you want them, allowing us to accommodate:</p>
  <ul class="checklist">
    <li><svg class="tick"><use href="#tick-mark"/></svg><span>All Food Allergies</span></li>
    <li><svg class="tick"><use href="#tick-mark"/></svg><span>Vegan Diets</span></li>
    <li><svg class="tick"><use href="#tick-mark"/></svg><span>Paleo Diets</span></li>
    <li><svg class="tick"><use href="#tick-mark"/></svg><span>Diets dictated by Personal Trainers &amp; Doctors</span></li>
    <li><svg class="tick"><use href="#tick-mark"/></svg><span>Or just plain picky eaters (you know who you are)</span></li>
  </ul>

  <div class="burst burst--price">
    <svg viewBox="0 0 100 100"><use href="#starburst" fill="#3fae3a"/></svg>
    <span>2 Fresh<br>Meals<br>$18/day!</span>
  </div>
  <div class="banner">100% Organic &amp; Gluten-Free Options Available</div>
</section>

<section class="card card--back">
  <div class="sunburst"></div>
  <div class="sunburst-fade"></div>
  <div class="figure figure--man" role="img" aria-label="Cartoon illustration of a fit man lifting a dumbbell with earphones"></div>

  <div class="wordmark"><i></i>Lean Plate Daily</div>
  <h2 class="reasons-title">
    <span class="light">Reasons Why</span>
    <span class="brand">Lean Plate Daily</span>
    <span class="light">is Awesome</span>
  </h2>
  <ul class="reasons">
    <li><svg class="tick"><use href="#tick-mark"/></svg><span>You get to choose your meals. We're here to help if you need us, but you won't get two of anything unless you ask for it!</span></li>
    <li><svg class="tick"><use href="#tick-mark"/></svg><span>No contracts or hefty monthly fees. Seriously, no need to even cancel - you only pay for what you order. Sound good? Fist bump?</span></li>
    <li><svg class="tick"><use href="#tick-mark"/></svg><span>We will be best friends! When you sign up with us, you get your own Lean Plate Daily advisor who will be by your side to help you make the right food choices and work with you to make us better for you. How cool is that!?</span></li>
    <li><svg class="tick"><use href="#tick-mark"/></svg><span>We will pay you to promote us! You're not hallucinating. We pay more than ANY other healthy meal delivery company out there. Not only that but we pay it for as long as your friends stay our friends! Ask your advisor for details.</span></li>
  </ul>

  <div class="photo photo--chicken" role="img" aria-label="Photo of grilled chicken over fresh salad greens"></div>
  <div class="burst burst--delivery">
    <svg viewBox="0 0 100 100"><use href="#starburst" fill="#3fae3a"/></svg>
    <span>FREE<br>Delivery<br>For Life!</span>
  </div>
  <div class="bubble">Call us today<br>to get started<br><span class="phone">833-415-2967</span></div>
  <p class="web-address">LeanPlateDaily.com</p>
</section>
</body>
</html>
```